Tolvek Card Design

IT consulting services - my company focuses on delivering value add for clients through sourcing services, strategic and project consulting services, as well as delivering office fitout project managment services.
We also offer IT Interim managment services - to fill the gap when looking for executive roles.
I use orange and blue as my corporate colours
I am after a simple design with my details on the front and my services not the back
Industry/Entity Type
It Company
Contact Information for Business Card
Martin Oskrey
Director
Tolvek Solutions
Martin.Oskrey@TolvekSolutions.com.au
www.TolvekSolutions.com.au
m: +61 427580916
On Rear of card:
Interim Management
Project and Strategy Consulting
Sourcing Services
Commercial fit-out management

```html
<!DOCTYPE html>
<html lang="en">
<head>
<meta charset="utf-8">
<title>Tolvek Solutions – Business Card</title>
<link rel="stylesheet" href="https://fonts.googleapis.com/css2?family=Arimo:wght@400;700&display=swap">
<style>
  :root {
    --stage: #9a9a98;
    --card: #121212;
    --orange: #de8a22;
    --blue: #1f3a6b;
    --white: #ffffff;
    --divider: #2c2c2c;
  }
  * { margin: 0; padding: 0; box-sizing: border-box; }
  html, body {
    width: 1200px;
    height: 726px;
    overflow: hidden;
    background: var(--stage);
    font-family: "Arimo", Arial, sans-serif;
  }
  .stage {
    position: relative;
    width: 1200px;
    height: 726px;
  }
  .card {
    position: absolute;
    top: 214px;
    width: 520px;
    height: 297px;
    background: var(--card);
    box-shadow: 0 6px 18px rgba(0,0,0,0.25);
    overflow: hidden;
  }
  .card--front { left: 50px; }
  .card--back { left: 630px; }

  .brand {
    position: absolute;
    display: flex;
    align-items: center;
    gap: 8px;
    color: var(--white);
    font-weight: 700;
    font-size: 19px;
  }
  .brand__square {
    width: 16px;
    height: 16px;
    background: var(--orange);
  }
  .card--front .brand { left: 36px; top: 98px; }
  .card--back .brand { left: 30px; top: 28px; font-size: 21px; }

  .divider {
    position: absolute;
    left: 262px;
    top: 50px;
    width: 1px;
    height: 200px;
    background: var(--divider);
  }
  .person {
    position: absolute;
    left: 282px;
    top: 62px;
    color: var(--orange);
    font-weight: 700;
    font-size: 16px;
    line-height: 1.1;
  }
  .contact {
    position: absolute;
    left: 282px;
    top: 140px;
    list-style: none;
    color: var(--orange);
    font-weight: 700;
    font-size: 11.5px;
    line-height: 25px;
  }

  .services {
    position: absolute;
    left: 34px;
    top: 72px;
    list-style: none;
    color: var(--orange);
    font-weight: 700;
    font-size: 13px;
    line-height: 17px;
  }
  .services li::before {
    content: "";
    display: inline-block;
    width: 4px;
    height: 4px;
    margin: 0 6px 2px 0;
    border-radius: 50%;
    background: var(--blue);
  }
</style>
</head>
<body>
  <main class="stage">
    <section class="card card--front" aria-label="Card front">
      <div class="brand"><span class="brand__square"></span>Tolvek Solutions</div>
      <div class="divider"></div>
      <div class="person">
        <p class="person__name">Martin Oskrey</p>
        <p class="person__role">Director</p>
      </div>
      <ul class="contact">
        <li>e: martin.oskrey@tolveksolutions.com.au</li>
        <li>m: +61 427 580 916</li>
        <li>w: www.tolveksolutions.com.au</li>
      </ul>
    </section>

    <section class="card card--back" aria-label="Card back">
      <div class="brand"><span class="brand__square"></span>Tolvek Solutions</div>
      <ul class="services">
        <li>Interim IT Management</li>
        <li>IT Project and Strategy Consulting</li>
        <li>Technology Sourcing Services</li>
        <li>Commercial fit-out management</li>
      </ul>
    </section>
  </main>
</body>
</html>
```